Talvor Visit cards serious but not sad

Hello, I'd like to design my visit cards with the logo Talvor (attached) the following information: Name: Karim Belmadi Title: Mobile Director: 33 (0) 6 72 18 35 09 Phone: 33 (0) 4 58 61 07 92 e-mail: karim.belmadi@talvor-consulting.example address: 17 Rue Marcel Danvin 92400 Courbevoie This visit will be used on the banking institutions and Talvor is a consulting firm. I do not want to have dark background.

Target Market(s)

banks

Contact Information for Business Card

Name : Karim Belmadi
Title : Director
mobile : +33(0)6 72 18 35 09
Phone : +33(0)4 58 61 07 92
e-mail: karim.belmadi@talvor-consulting.example
adresse : 17 Rue marcel Danvin 92870 Vallermont

Requirements
Nice to have
• serious but not sad

```html
<!DOCTYPE html>
<html lang="en">
<head>
<meta charset="utf-8">
<title>Talvor – Business Card</title>
<link rel="stylesheet" href="https://fonts.googleapis.com/css2?family=Exo+2:wght@400;500;600&family=Roboto+Condensed:wght@400&display=swap">
<style>
  :root {
    --backdrop: #e6e8eb;
    --card: #ffffff;
    --brand: #1565b5;
    --brand-light: #3b86c8;
    --brand-dark: #0a58a6;
    --ink: #1d1d1f;
    --on-brand: #ffffff;
  }
  * { box-sizing: border-box; margin: 0; padding: 0; }
  html, body {
    width: 1200px; height: 815px; overflow: hidden;
    background: var(--backdrop);
  }
  .card {
    position: absolute; left: 150px; top: 116px;
    width: 900px; height: 582px;
    background: var(--card);
    box-shadow: 0 6px 24px rgba(0,0,0,0.12);
  }
  .brand {
    position: absolute; top: 52px; right: 88px;
    display: flex; align-items: center; gap: 14px;
  }
  .brand-dot {
    width: 84px; height: 84px; border-radius: 50%;
    background: var(--brand);
  }
  .brand-name {
    font-family: "Exo 2", sans-serif; font-weight: 600;
    font-size: 56px; color: var(--brand); letter-spacing: 1px;
  }
  .name-band {
    position: absolute; left: 0; right: 0; top: 170px; height: 140px;
    background: linear-gradient(90deg, var(--brand-light) 0%, var(--brand) 55%, var(--brand-dark) 100%);
    padding: 50px 0 0 62px;
    color: var(--on-brand);
  }
  .holder-name {
    font-family: "Exo 2", sans-serif; font-weight: 400;
    font-size: 44px; line-height: 1; letter-spacing: 1px;
  }
  .holder-title {
    font-family: "Exo 2", sans-serif; font-weight: 500;
    font-size: 21px; letter-spacing: 3px; margin-top: 10px;
    margin-left: 12px; text-transform: uppercase;
  }
  .contacts {
    position: absolute; left: 76px; top: 358px;
    font-family: "Roboto Condensed", sans-serif; font-size: 27px;
    color: var(--ink);
  }
  .contact-row { display: flex; align-items: center; gap: 56px; margin-bottom: 12px; }
  .contact { display: flex; align-items: center; gap: 14px; }
  .icon { width: 36px; height: 36px; flex: none; }
</style>
</head>
<body>
  <div class="card">
    <div class="brand">
      <span class="brand-dot"></span>
      <span class="brand-name">Talvor</span>
    </div>

    <div class="name-band">
      <p class="holder-name">Karim Belmadi</p>
      <p class="holder-title">Director</p>
    </div>

    <div class="contacts">
      <div class="contact-row">
        <div class="contact">
          <svg class="icon" viewBox="0 0 36 36" aria-hidden="true">
            <circle cx="18" cy="18" r="18" fill="var(--brand)"/>
            <path d="M18 8a7 7 0 0 0-7 7c0 5 7 13 7 13s7-8 7-13a7 7 0 0 0-7-7z" fill="#fff"/>
            <circle cx="18" cy="15" r="2.6" fill="var(--brand)"/>
          </svg>
          <span>17 Rue marcel Danvin 92870 Vallermont</span>
        </div>
      </div>
      <div class="contact-row">
        <div class="contact">
          <svg class="icon" viewBox="0 0 36 36" aria-hidden="true">
            <circle cx="18" cy="18" r="18" fill="var(--brand)"/>
            <rect x="9" y="12" width="18" height="12" rx="1" fill="none" stroke="#fff" stroke-width="2"/>
            <path d="M9 12l9 7 9-7" fill="none" stroke="#fff" stroke-width="2"/>
          </svg>
          <span>karim.belmadi@talvor-consulting.example</span>
        </div>
      </div>
      <div class="contact-row">
        <div class="contact">
          <svg class="icon" viewBox="0 0 36 36" aria-hidden="true">
            <circle cx="18" cy="18" r="18" fill="var(--brand)"/>
            <rect x="13" y="8" width="10" height="20" rx="2" fill="none" stroke="#fff" stroke-width="2"/>
            <circle cx="18" cy="24.5" r="1.2" fill="#fff"/>
          </svg>
          <span>+33(0)6 72 18 35 09</span>
        </div>
        <div class="contact">
          <svg class="icon" viewBox="0 0 36 36" aria-hidden="true">
            <circle cx="18" cy="18" r="18" fill="var(--brand)"/>
            <path d="M12 9l4 0 2 5-2.5 2a12 12 0 0 0 5.5 5.5l2-2.5 5 2v4c0 1-1 2-2 2C17 27 9 19 9 11c0-1 1-2 3-2z" fill="#fff"/>
          </svg>
          <span>+33(0)4 58 61 07 92</span>
        </div>
      </div>
    </div>
  </div>
</body>
</html>
```